Detail Shop Menu Board for Walk In Clients

I am looking to have digital menus for my detail shop. I have 3 55-inch TVs on the wall for my front desk area. They will be vertical on the wall, not horizontal, so the design needs to be vertical.

Color pallet I am looking for is black and gold, with some accent colors if applicable. I would like black background with some sort of design in it in such a way it looks faint or ghosted in the background ... i.e., honeycomb, splatter, etc. A boarder is optional.

Needs to be designed well, organized well and easy to read for customers walking in.

the each category is for each TV: Interior and Maintenance plans, Exterior and Ceramic Coatings

Company logo files included. would like my logos on them as well.

This job will need another menu board done in the future as well.

Industry/Entity Type

Auto Detailing

Requirements
Should not have
• no dollar signs ($) on any pricing

```html
<!DOCTYPE html>
<html lang="en">
<head>
<meta charset="utf-8">
<title>Forgewell Garage Service Menus</title>
<link href="https://fonts.googleapis.com/css2?family=Montserrat:wght@400;500;600;700&display=swap" rel="stylesheet">
<style>
  :root{
    --stage:#ececec;
    --board:#050505;
    --heading:#d99a2b;
    --item:#eccb6a;
    --white:#f4f4f4;
    --silver:#b9b9b9;
    --gold-hi:#e9c46e;
    --gold-lo:#b98428;
  }
  *{box-sizing:border-box;margin:0;padding:0}
  html,body{width:900px;height:1200px;overflow:hidden;background:var(--stage)}
  body{position:relative;font-family:"Montserrat",Arial,sans-serif}
  .board{position:absolute;width:663px;height:995px;background:var(--board);transform:scale(.543);transform-origin:0 0;overflow:hidden;color:var(--white)}
  .board--exterior{left:49px;top:45px}
  .board--interior{left:493px;top:45px}
  .board--maintenance{left:49px;top:629px}
  .board--ceramic{left:493px;top:629px}
  .photo{position:absolute}
  .brand{position:absolute;width:170px;text-align:center}
  .brand__dot{width:44px;height:44px;border-radius:50%;background:var(--silver);margin:0 auto 14px}
  .brand__name{font-size:19px;font-weight:600;color:var(--silver);letter-spacing:1px;line-height:1.2}
  .blk{position:absolute;left:42px;right:42px}
  .h{font-size:16px;font-weight:700;color:var(--heading);line-height:1.15;letter-spacing:.2px}
  .sub{font-size:14px;font-weight:600;color:var(--white);line-height:1.25;margin-top:8px}
  .note{font-size:12.5px;color:var(--item);line-height:1.3}
  .items{list-style:none;display:grid;grid-template-columns:1fr 1fr;column-gap:14px;row-gap:8px;margin-top:10px}
  .items li,.list li{font-size:12.5px;color:var(--item);line-height:1.2;padding-left:11px;position:relative}
  .items li::before,.list li::before{content:"•";position:absolute;left:0}
  .items .wide{grid-column:1 / -1}
  .list{list-style:none}
  .list li{margin-bottom:13px}
  .list b{font-weight:700}
  .rows li{height:27.7px;margin:0}
  .m-items{row-gap:13px}
  .blob{position:absolute;left:330px;top:388px;width:320px;height:318px}
  .blob__text{position:absolute;left:375px;top:418px;width:230px;text-align:center;color:#1d1305}
  .blob__text .t{font-size:15px;font-weight:700;color:#f3d58a;line-height:1.2}
  .blob__text .r{font-size:13.5px;font-weight:600;color:#fff;margin:12px 0 10px}
  .blob__text li{list-style:none;font-size:12.5px;line-height:1.2;margin-bottom:13px}
  .addons{position:absolute;left:105px;top:775px;width:330px;height:195px;border-radius:40px 8px 50px 10px;background:linear-gradient(100deg,var(--gold-lo),var(--gold-hi) 55%,var(--gold-lo))}
  .addons__text{position:absolute;left:105px;top:795px;width:330px;text-align:center;color:#111;font-weight:600;font-size:14px;line-height:1.25}
  .addons__text .t{font-weight:700;font-size:15px;margin-bottom:8px}
  .addons__text p{margin-bottom:8px}
  .ceramic p.desc{font-size:12.5px;color:var(--white);line-height:1.25;text-align:justify;margin-top:4px}
  .ceramic .lvl{font-size:12.5px;font-weight:700;color:var(--item);margin-top:14px}
  .ceramic .other{font-size:12.5px;color:var(--white);line-height:1.25;text-align:justify;margin-top:10px}
  .ceramic .other b{color:var(--item);font-weight:700}
</style>
</head>
<body>

<!-- Exterior -->
<section class="board board--exterior">
  <div class="photo" role="img" aria-label="Dark studio photo of a sports car front with headlights" style="left:0;top:0;width:200px;height:230px;background:radial-gradient(ellipse at 40% 50%,#6d6d6d 0%,#2a2a2a 40%,#050505 75%)"></div>
  <div class="brand" style="left:220px;top:80px"><div class="brand__dot"></div><div class="brand__name">FORGEWELL GARAGE</div></div>

  <div class="blk" style="top:260px">
    <h2 class="h">BASIC EXTERIOR DETAIL:</h2>
    <p class="sub">Cars: 100, Midsize 125, Trucks/SUVs 150 and up (+tax)</p>
    <ul class="items" style="row-gap:11px;grid-template-columns:1.25fr 1fr">
      <li>Standard Hand wash</li><li>Wheels/Wheel wells cleaned</li>
      <li>Exterior plastics dressing</li><li>Tire dressing</li>
      <li>Window cleaning</li><li>Spray wax</li>
    </ul>
  </div>

  <div class="blk" style="top:398px">
    <h2 class="h">COMPLETE EXTERIOR DETAIL:</h2>
    <p class="sub">Cars: 180, Midsize 220, Truck/SUV 260 (+tax)</p>
    <ul class="items" style="row-gap:11px;grid-template-columns:1.25fr 1fr">
      <li>Standard hand wash</li><li>Iron decontamination</li>
      <li class="wide">Clay bar treatment to remove environmental contamination (sap, tar, etc),</li>
      <li>Tires, wheels, wheel wells cleaned and dressed</li><li>Door jams cleaned</li>
      <li>Trunk lid/Rear Hatch, gas cap area cleaned</li><li>Exterior glass cleaned</li>
      <li>Black plastics dressed</li><li>SiO2 protection</li>
    </ul>
  </div>

  <div class="blk" style="top:588px">
    <h2 class="h">EXECUTIVE EXTERIOR DETAIL &amp; EXPRESS COATING:</h2>
    <p class="sub">Cars: 350, Midsize 400, Truck/SUV 450 and up (+tax)</p>
    <ul class="list" style="margin-top:6px"><li>Complete Exterior Detail PLUS 1yr Ceramic Coating</li></ul>
  </div>

  <div class="blk" style="top:694px;right:auto;width:290px">
    <h2 class="h">EXTERIOR MULTI-STEP PAINT CORRECTION:</h2>
    <p class="sub">Price By Quote Only</p>
    <p class="note" style="font-weight:600;margin:26px 0 8px">Exterior Add On's:</p>
    <ul class="list">
      <li><b>Complete Wheel Detail:</b> Wheels off, deep cleaned and protected inside and out, reinstalled and torqued to factory spec: 150 and up</li>
      <li><b>Headlight Restoration:</b> 100 and up</li>
      <li><b>Water Spot Removal:</b> 50/hr</li>
      <li><b>Plastic Trim Restoration:</b> 50 and up</li>
    </ul>
  </div>

  <div class="blk" style="top:694px;left:368px;right:30px">
    <h2 class="h">POLISHING &amp; PAINTWORK</h2>
    <p class="sub">Exterior Enhancement Detail:<br>Cars 350, Midsize 400<br>Trucks/SUVs<br>450 and up (+ tax)</p>
    <ul class="list" style="margin-top:12px">
      <li>Our Complete Exterior Package plus:</li>
      <li>Single step polish</li>
      <li>Upgraded paint sealant</li>
      <li>Upgraded durable, long-lasting tire and trim dressing</li>
      <li>Windshield Protection</li>
    </ul>
  </div>
</section>

<!-- Interior -->
<section class="board board--interior">
  <div class="photo" role="img" aria-label="Dark photo of a car interior with steering wheel and dashboard" style="left:0;top:0;width:460px;height:240px;background:radial-gradient(ellipse at 40% 35%,#5a5a5a 0%,#262626 45%,#050505 80%)"></div>
  <div class="brand" style="left:315px;top:170px"><div class="brand__dot"></div><div class="brand__name">FORGEWELL GARAGE</div></div>

  <div class="blk" style="top:260px;right:auto;width:300px">
    <h2 class="h">INTERIOR DETAILING PACKAGES</h2>
    <p class="sub">Deluxe Interior Clean:</p>
    <p class="sub" style="font-weight:500;margin-top:10px">Hourly Shop Rate at 85/hr (+tax)</p>
    <ul class="list" style="margin-top:12px">
      <li>Full vacuum of carpet, seats, upholstery</li>
      <li>Floormats treated and steam cleaned</li>
      <li>Dash/doors scrubbed, wiped down and dressed</li>
      <li>Clean console, cup holders, crevices and vents</li>
      <li>Clean dash and UV protectant</li>
      <li>Clean all interior trim and plastics</li>
      <li>Clean and condition door panels and pockets</li>
      <li>Clean door jambs and weather stripping</li>
      <li>Clean glass surfaces</li>
      <li>Lightly clean vehicle headliner and sun visors</li>
      <li>Shampoo cloth seats</li>
      <li>Deep clean and condition leather seats</li>
      <li>Apply protective treatment to leather and vinyl</li>
      <li>Trunk and spare tire areas also cleaned</li>
    </ul>
  </div>

  <svg class="blob" viewBox="0 0 320 318" aria-hidden="true">
    <defs><linearGradient id="blobGold" x1="0" y1="0" x2="0" y2="1"><stop offset="0" stop-color="#e7c36c"/><stop offset="1" stop-color="#a8721f"/></linearGradient></defs>
    <path d="M160 4 C210 0 250 30 285 55 C320 95 318 150 314 200 C310 250 280 300 220 312 C170 320 110 318 70 300 C20 275 0 220 4 160 C8 100 30 50 80 22 C105 8 130 6 160 4Z" fill="url(#blobGold)"/>
  </svg>
  <div class="blob__text">
    <p class="t">BASIC INTERIOR<br>CLEAN:</p>
    <p class="r">Hourly Shop Rate at 85/hr</p>
    <ul>
      <li>Full vacuum of carpet, seats, upholstery</li>
      <li>Floormats treated and steam cleaned</li>
      <li>Dash/doors lightly wiped down and dressed</li>
      <li>Interior glass surfaces cleaned</li>
      <li>Steering wheel and center console scrubbed and cleaned</li>
    </ul>
  </div>

  <div class="addons" role="img" aria-label="Gold paint brush stroke"></div>
  <div class="addons__text">
    <p class="t">INTERIOR ADD ONS:</p>
    <p>Ozone Treatment: 50</p>
    <p>• Fabric Guard:<br>100 per row</p>
    <p>BioHazard Cleaning:<br>• 500 per row</p>
  </div>
</section>

<!-- Maintenance -->
<section class="board board--maintenance">
  <div class="photo" role="img" aria-label="Dark photo of a car center console and controls" style="left:0;top:0;width:360px;height:260px;background:radial-gradient(ellipse at 35% 40%,#4a4f55 0%,#1f2225 45%,#050505 80%)"></div>
  <div class="photo" role="img" aria-label="Faint photo of a car interior with dashboard and seats" style="left:0;top:380px;width:663px;height:615px;background:radial-gradient(ellipse at 70% 45%,#2a2a2c 0%,#131315 45%,#050505 80%)"></div>
  <div class="brand" style="left:325px;top:170px"><div class="brand__dot"></div><div class="brand__name">FORGEWELL GARAGE</div></div>

  <div class="blk" style="top:283px">
    <h2 class="h">MAINTENANCE PLANS</h2>
    <p class="note" style="margin-top:10px;text-align:justify">All maintenance plans <b style="color:var(--white)">start with a Complete Exterior Detail and Deluxe Interior Detail</b> to provide a clean, fresh start. After that has been performed, we will schedule you for your follow up maintenance program.</p>
  </div>

  <div class="blk" style="top:385px">
    <h2 class="h">MONTHLY MAINTENANCE DETAIL:</h2>
    <p class="sub">Cars 100, Midsize 125 Trucks/SUVs 150 and up (+ tax)</p>
    <ul class="items m-items">
      <li>Pre rinse</li><li>Hand wash</li>
      <li>Wheels/Wheel wells cleaned</li><li>Exterior plastics dressing</li>
      <li>Tire dressing</li><li>Window cleaning</li>
      <li>Spray on protection</li><li>Interior vacuum</li>
      <li>Interior wiped down &amp; dressing</li><li>All Glass cleaned</li>
    </ul>
  </div>

  <div class="blk" style="top:600px">
    <h2 class="h">MONTHLY MAINTENANCE DETAIL:</h2>
    <p class="sub">Cars 100, Midsize 125 Trucks/SUVs 150 and up (+ tax)</p>
    <ul class="items m-items">
      <li>Pre rinse</li><li>Hand wash</li>
      <li>Bug/Tar Removal</li><li>Wheels/Wheel wells cleaned</li>
      <li>Exterior plastics dressing</li><li>Tire dressing</li>
      <li>Window cleaning</li><li>Spray on protection</li>
      <li>Interior vacuum</li><li>All Glass cleaned</li>
      <li>Spot Treatment for Stains, etc</li><li>Interior wiped down &amp; dressing</li>
    </ul>
  </div>
</section>

<!-- Ceramic -->
<section class="board board--ceramic ceramic">
  <div class="photo" role="img" aria-label="Dark photo of a car center console and controls" style="left:0;top:0;width:360px;height:260px;background:radial-gradient(ellipse at 35% 40%,#4a4f55 0%,#1f2225 45%,#050505 80%)"></div>
  <div class="photo" role="img" aria-label="Dark photo of hands applying ceramic coating to a car panel" style="left:0;top:760px;width:520px;height:235px;background:radial-gradient(ellipse at 35% 50%,#3a3a30 0%,#18180f 45%,#050505 80%)"></div>
  <div class="brand" style="left:315px;top:170px"><div class="brand__dot"></div><div class="brand__name">FORGEWELL GARAGE</div></div>

  <div class="blk" style="top:283px">
    <h2 class="h">CERAMIC COATINGS</h2>
    <p class="sub">Bespoke Ceramic Coating Package: Starting at 3000.</p>
    <p class="lvl">One Word: Perfection.</p>
    <p class="lvl">Platinum Level Coating: Cars: 1300, Midsize: 1500, Trucks/SUVs: 1700 (+ tax)</p>
    <p class="desc">Warrantied paint coating, applied to all painted surfaces, plastic trim, and wheel faces. provides up to 60 months (50-60k miles) of durability when maintained properly</p>
    <p class="lvl">Gold Level Coating: Cars: 900, Midsize: 1000, Trucks/SUVs: 1100 (+ tax)</p>
    <p class="desc">Durable paint coating applied to all painted surfaces and plastic trim, provides up to 36 months (30-36k miles) of durability when maintained properly</p>
    <p class="lvl">Entry Level Coating: Cars: 600, Midsize: 700, Trucks/SUVs: 800 (+tax)</p>
    <p class="desc">Coating applied to all painted surfaces, provides up to a 12-month (10-12k miles) lifespan of durability. Add a second layer for 100 more for 18-24 months (20k-24k miles) of protection</p>

    <h2 class="h" style="margin-top:28px">OTHER COATINGS OFFERED:</h2>
    <p class="other"><b>Wheel Coating:</b> 50/wheel and up: Wheel face coated with one layer of ceramic giving you up to 9-12 months of protection. 2 layers will yield 12-18+ months of protection. *Raw aluminum wheels CAN NOT be coated.</p>
    <p class="other"><b>Wheel Off Coating:</b> 400 and up: Wheel coating package + durable industrial coating on barrels of wheels and if applicable, calipers and suspension components.</p>
    <p class="other"><b>Windshield Coating:</b> 100 and up: Glass is polished to remove any stuck-on contamination and treated with a coating that lasts 6 months to a year+. Lifespan of the coating is in relation to wiper use and environment.</p>
  </div>
</section>

</body>
</html>
```